Child-Biting, Chorizo and Chancing Your Arm

Looking to get a book cover designed.

I am an entrepreneur with an edge (I am fun, outgoing and with tons of personality) and run a localisation company called Tonglingo. My book is my story, some business lessons and also some language lessons and idioms. I am an entrepreneur who has set up his business in a country other than his, with a different language - and thus my book talks about communication and the problems that do arise when things get lost in translation.

I have included, attached, a document with three forewords/introductions from others about the book.

The title of the book is:

Child-Biting,
Chorizo
and Chancing Your Arm
(whatever that means) [in small letters]

And the subtitle:
How a lonely Spaniard made it big in Britain

Notes:

I was a child biter
I am from Spain - thus chorizo
And I set a business up in the UK - took a risk "chance my arm"

Also, may be a good idea (depends how it looks) to have "whatever that means" in small letters after chancing your arm, since most English people do not know the meaning of this expression. And I constantly play on words with communication throughout the book.

Style notes:

The book is fun, entertaining and I do not take myself too seriously, so I want the cover to be professional, bold and striking.

I like the colours black and red, but these are not a must. The idea is to make the cover stand out, while still remain professional.

--------
Chancing Your Arm: http://www.brennockabbey.example/chancing-your-arm.aspx

Target Market(s)

Entrepreneurs, business owners, linguists, people that work in large organisations but appreciate a bit of a human/personal touch.

Industry/Entity Type

Business

Font styles to use
Sans Serif
Other font styles liked:
• Modern font.

Colors
ec1f27
ffffff
000000
d5d5d5
0355a3

Requirements
Nice to have
• Bold statement
• Striking but classy
• Fun
• Different
• Stand out
Should not have
• Traditional boring style
• Yellow colour

```html
<!DOCTYPE html>
<html lang="en">
<head>
<meta charset="utf-8">
<title>Child-Biting, Chorizo and Chancing Your Arm — Book Cover</title>
<link rel="stylesheet" href="https://fonts.googleapis.com/css2?family=Chewy&family=Oswald:wght@500&family=Open+Sans:wght@400&display=swap">
<style>
  :root {
    --ink: #0b0b0c;
    --metal-dark: #141416;
    --metal-light: #2c2c30;
    --title-red: #d8141c;
    --title-red-deep: #8e0a10;
    --title-red-light: #ff4a4a;
    --gold: #e6b443;
    --pink: #e8176f;
    --cyan: #74c7ec;
    --splash-red: #e0161f;
    --splash-blue: #1f6fc0;
    --subtitle-pink: #e8176f;
    --subtitle-blue: #42a9e2;
    --author-blue: #1c63b0;
    --author-blue-light: #2f7fd0;
    --sausage: #b52c20;
    --sausage-dark: #7a1610;
  }
  * { box-sizing: border-box; margin: 0; padding: 0; }
  html, body { width: 750px; height: 1200px; overflow: hidden; background: var(--ink); }

  .cover {
    position: relative;
    width: 750px;
    height: 1200px;
    overflow: hidden;
    background:
      repeating-linear-gradient(90deg,
        rgba(255,255,255,0.035) 0 1px, transparent 1px 3px,
        rgba(0,0,0,0.25) 3px 4px, transparent 4px 7px),
      radial-gradient(ellipse at 55% 45%, var(--metal-light) 0%, var(--metal-dark) 60%, #070708 100%);
  }

  .splatter { position: absolute; pointer-events: none; }
  .splatter--red { top: 0; left: 0; width: 260px; height: 520px; }
  .splatter--blue { right: 0; bottom: 0; width: 220px; height: 560px; }

  .divider {
    position: absolute;
    left: 0; right: 0;
    height: 2px;
    background: linear-gradient(90deg, transparent, rgba(0,0,0,0.7) 10%, rgba(0,0,0,0.7) 90%, transparent);
    box-shadow: 0 1px 0 rgba(255,255,255,0.08);
  }

  .flare {
    position: absolute;
    height: 12px;
    border-radius: 50%;
    background: radial-gradient(ellipse, rgba(255,160,90,0.9) 0%, rgba(255,60,20,0.55) 30%, transparent 70%);
    filter: blur(1px);
  }

  .book-title { font-weight: 400; }
  .title {
    position: absolute;
    left: 0; right: 0;
    text-align: center;
    font-family: "Chewy", "Comic Neue", sans-serif;
    font-weight: 400;
    line-height: 1;
    white-space: nowrap;
  }
  .title-line {
    position: relative;
    display: inline-block;
    vertical-align: middle;
    color: var(--title-red);
    background: linear-gradient(180deg, var(--title-red-light) 0%, var(--title-red) 45%, var(--title-red-deep) 100%);
    -webkit-background-clip: text;
    background-clip: text;
    -webkit-text-fill-color: transparent;
    -webkit-text-stroke: 3px var(--gold);
    filter: drop-shadow(0 0 10px rgba(230,30,30,0.45));
  }
  .title-line::before,
  .title-line::after {
    content: attr(data-text);
    position: absolute;
    left: 0; top: 0;
    z-index: -1;
    -webkit-text-fill-color: transparent;
    background: none;
  }
  .title-line::before { -webkit-text-stroke: 3px var(--pink); transform: translate(-3px, 4px); }
  .title-line::after  { -webkit-text-stroke: 3px var(--cyan); transform: translate(-7px, 9px); }

  .title--line1 { top: 222px; font-size: 108px; }
  .title--line2 { top: 390px; font-size: 108px; }
  .title--line3 { top: 554px; font-size: 108px; }
  .title--line4 { top: 712px; font-size: 104px; }
  .title--aside { top: 858px; font-size: 62px; }
  .title--aside .title-line::before,
  .title--aside .title-line::after { display: none; }
  .title--aside .title-line { -webkit-text-stroke: 2px var(--gold); }

  .chorizo-slice {
    display: inline-block;
    vertical-align: middle;
    width: 70px;
    height: 80px;
    margin: 0 4px 0 2px;
    border-radius: 50%;
    background: radial-gradient(ellipse, transparent 0 26%, var(--sausage) 28%, #cf4030 60%, var(--sausage-dark) 70%, transparent 72%);
  }

  .subtitle {
    position: absolute;
    font-family: "Open Sans", sans-serif;
    font-weight: 400;
    font-size: 26px;
    white-space: nowrap;
  }
  .subtitle--first { left: 238px; top: 936px; color: var(--subtitle-pink); }
  .subtitle--second { left: 390px; top: 970px; color: var(--subtitle-blue); transform: rotate(-4deg); transform-origin: left center; }

  .author {
    position: absolute;
    left: 0; right: 0;
    top: 1070px;
    text-align: center;
    font-family: "Oswald", "Arial Narrow", sans-serif;
    font-weight: 500;
    font-size: 92px;
    line-height: 1;
    letter-spacing: -1px;
    color: var(--author-blue);
    background: linear-gradient(180deg, var(--author-blue-light) 0%, var(--author-blue) 55%, #15508f 100%);
    -webkit-background-clip: text;
    background-clip: text;
    -webkit-text-fill-color: transparent;
  }
</style>
</head>
<body>
<main class="cover">
  <svg class="splatter splatter--red" viewBox="0 0 260 520" aria-hidden="true">
    <g fill="var(--splash-red)">
      <ellipse cx="20" cy="10" rx="60" ry="40" opacity="0.5"/>
      <circle cx="50" cy="50" r="12" opacity="0.7"/>
      <circle cx="100" cy="28" r="5"/><circle cx="140" cy="70" r="3"/>
      <circle cx="18" cy="110" r="7" opacity="0.8"/><circle cx="8" cy="170" r="4"/>
      <circle cx="90" cy="120" r="3"/><circle cx="180" cy="40" r="2.5"/>
      <circle cx="14" cy="240" r="4" opacity="0.8"/><circle cx="30" cy="300" r="2"/>
      <circle cx="6" cy="360" r="3"/><circle cx="40" cy="420" r="2"/>
      <circle cx="220" cy="20" r="2"/><circle cx="70" cy="180" r="2"/>
      <circle cx="160" cy="110" r="2"/><circle cx="50" cy="230" r="1.5"/>
    </g>
  </svg>
  <svg class="splatter splatter--blue" viewBox="0 0 220 560" aria-hidden="true">
    <g fill="var(--splash-blue)">
      <ellipse cx="225" cy="555" rx="50" ry="45" opacity="0.45"/>
      <circle cx="200" cy="490" r="5" opacity="0.8"/>
      <circle cx="160" cy="530" r="3"/><circle cx="210" cy="420" r="4" opacity="0.8"/>
      <circle cx="180" cy="440" r="2"/><circle cx="130" cy="545" r="2"/>
      <circle cx="205" cy="320" r="3"/><circle cx="180" cy="260" r="2"/>
      <circle cx="150" cy="470" r="1.5"/><circle cx="210" cy="180" r="2"/>
      <circle cx="175" cy="360" r="1.5"/><circle cx="195" cy="80" r="1.5"/>
    </g>
  </svg>

  <div class="divider" style="top:372px"></div>
  <div class="divider" style="top:548px"></div>
  <div class="divider" style="top:708px"></div>

  <div class="flare" style="left:70px;top:730px;width:200px"></div>
  <div class="flare" style="left:480px;top:770px;width:220px"></div>

  <h1 class="book-title">
    <span class="title title--line1"><span class="title-line" data-text="Child-Biting,">Child-Biting,</span></span>
    <span class="title title--line2"><span class="title-line" data-text="Ch">Ch</span><span class="chorizo-slice" role="img" aria-label="Ring of chorizo slices forming the letter O"></span><span class="title-line" data-text="rizo">rizo</span></span>
    <span class="title title--line3"><span class="title-line" data-text="and Chancing">and Chancing</span></span>
    <span class="title title--line4"><span class="title-line" data-text="Your Arm">Your Arm</span></span>
    <span class="title title--aside"><span class="title-line" data-text="whatever that mean?">whatever that mean?</span></span>
  </h1>

  <p class="subtitle subtitle--first">How a lonely Spaniard</p>
  <p class="subtitle subtitle--second">made it big in Britain</p>

  <p class="author">AUTHOR NAME</p>
</main>
</body>
</html>
```